Lantern Motion for Neighbors Business Cards

I need business cards for staff in a new startup. Our company name is Movrela - we train Tai Chi teachers. But our biggest project is called Lantern Motion for Neighbors - a federal project to put together free Tai Chi classes for Vets all across America. It's a young company, with a spirit of excitement, passion, a desire to do good for others (our Vets) and a modern style and sensibility. In other words, not old-fashioned Asian martial arts theme, but something new.

Industry/Entity Type

Health And Wellness

Contact Information for Business Card

The topic is ancient healing, but the company is the Pembrooks - so I'd like a card design that captures that.

Font styles to use
Sans Serif

Colors

Designer to choose colors to be used in the design.

Requirements
Nice to have
• I've got two logos - one for the company and one for the project. I want to see if we can incorporate them both without it becoming too busy.
Should not have
• Overly old-fashioned yin-yang themes.

```html
<!DOCTYPE html>
<html lang="en">
<head>
<meta charset="utf-8">
<title>Movrela Business Card</title>
<link href="https://fonts.googleapis.com/css2?family=Lato:wght@400;700;900&display=swap" rel="stylesheet">
<style>
  :root {
    --backdrop: #ecebe9;
    --red-top: #c0232f;
    --red-mid: #a51d28;
    --red-deep: #4a0a0f;
    --sun-yellow: #f1ee7d;
    --ink-white: #ffffff;
    --soft-white: rgba(255, 255, 255, 0.9);
    --mark-red: #d9231f;
    --mark-ink: #2a1a1a;
  }
  * { margin: 0; padding: 0; box-sizing: border-box; }
  html, body {
    width: 1200px;
    height: 900px;
    overflow: hidden;
    background: var(--backdrop);
    font-family: "Lato", sans-serif;
  }
  .business-card {
    position: absolute;
    left: 275px;
    top: 247px;
    width: 650px;
    height: 405px;
    overflow: hidden;
    box-shadow: 0 14px 40px rgba(0, 0, 0, 0.22);
  }
  .card-field {
    position: absolute;
    left: 0;
    top: 0;
    width: 440px;
    height: 100%;
    background: linear-gradient(180deg, var(--red-top) 0%, var(--red-mid) 45%, var(--red-deep) 100%);
  }
  .card-strip {
    position: absolute;
    left: 440px;
    top: 0;
    width: 210px;
    height: 100%;
    background: var(--sun-yellow);
  }
  .contact-block {
    position: absolute;
    left: 37px;
    top: 44px;
    color: var(--ink-white);
  }
  .person-name {
    font-weight: 900;
    font-size: 22px;
    letter-spacing: 0.3px;
    line-height: 26px;
  }
  .person-role {
    font-size: 17px;
    line-height: 22px;
  }
  .contact-list {
    list-style: none;
    margin-top: 22px;
  }
  .contact-list li {
    display: flex;
    align-items: center;
    gap: 7px;
    font-size: 17px;
    line-height: 24px;
  }
  .contact-list svg { width: 14px; height: 14px; flex: none; }
  .postal-address {
    margin-top: 18px;
    font-style: normal;
    font-size: 17px;
    line-height: 24px;
    padding-left: 2px;
  }
  .project-name {
    position: absolute;
    left: 37px;
    top: 278px;
    display: flex;
    align-items: center;
    gap: 10px;
    color: var(--ink-white);
    font-size: 16px;
    font-weight: 400;
    line-height: 19px;
    letter-spacing: 0.6px;
    text-transform: uppercase;
  }
  .project-name .plain-dot {
    width: 46px;
    height: 46px;
    border: 1.5px solid var(--ink-white);
    border-radius: 50%;
    flex: none;
  }
  .brand-disc {
    position: absolute;
    left: 269px;
    top: 27px;
    width: 346px;
    height: 346px;
    border-radius: 50%;
    background: radial-gradient(circle at 50% 45%, rgba(255,255,255,0.96) 0%, rgba(244,242,240,0.9) 70%, rgba(226,224,222,0.88) 100%);
    display: flex;
    align-items: center;
    justify-content: center;
    gap: 12px;
  }
  .brand-disc .plain-dot {
    width: 78px;
    height: 78px;
    border-radius: 50%;
    background: var(--mark-red);
  }
  .brand-name {
    font-size: 34px;
    font-weight: 700;
    color: var(--mark-red);
  }
</style>
</head>
<body>
  <div class="business-card">
    <div class="card-field"></div>
    <div class="card-strip"></div>

    <div class="contact-block">
      <h1 class="person-name">DANIEL HARROW</h1>
      <p class="person-role">Managing Director</p>
      <ul class="contact-list">
        <li>
          <svg viewBox="0 0 16 16" aria-hidden="true"><path fill="#fff" d="M2 6c0-2 2-3 6-3s6 1 6 3v1h-3V5.5H5V7H2zM4 8h8l1.5 5h-11z"/></svg>
          044-987 310 552
        </li>
        <li>
          <svg viewBox="0 0 16 16" aria-hidden="true"><rect x="1" y="3" width="14" height="10" fill="#fff"/><path d="M1 3l7 6 7-6" fill="none" stroke="#a51d28" stroke-width="1.3"/></svg>
          hello@movrela.com
        </li>
        <li>
          <svg viewBox="0 0 16 16" aria-hidden="true"><circle cx="8" cy="8" r="7" fill="#fff"/><path d="M5 4l3 2-1 3 2 2-1 3M10 3l1 3 2 1" fill="none" stroke="#a51d28" stroke-width="1.2"/></svg>
          www.movrela.com
        </li>
      </ul>
      <address class="postal-address">58, Willow Lane West,<br>30817,United States</address>
    </div>

    <div class="project-name">
      <span class="plain-dot"></span>
      <span>Lantern Motion<br>for Neighbors</span>
    </div>

    <div class="brand-disc">
      <span class="plain-dot"></span>
      <span class="brand-name">Movrela</span>
    </div>
  </div>
</body>
</html>
```